Business Card Design - BVN (company name)

Over 20 years of progressive technology design, migration and management experience that drives business objectives and streamlines operations. Continuously challenge conventions to meet and exceed business security, availability and functionality requirements. Maintain exceptional vendor relationships to ensure ongoing knowledge of emerging products and to secure preferred service agreements. Recruit and utilize top talent and foster a collegial environment that advances innovation and performance excellence. design logo using 3 arrows of different colors green, gold, blue

Industry/Entity Type

Progressive

Contact Information for Business Card

Martin K. Osei
IT Strategist / Consultant

555.302.8846 MOsei@bvnorel.example 3817 Wrenfield Court Pasadena, CA 91877

Colors
0255a3
f37122
fece3e

Requirements
Must have
• Note NEW EMAIL ADDRESS
• MOsei@bvnorel.example
• NOTE NEW ORDER of the work I do.
• Infrastructure – Systems – Cybersecurity
Nice to have
• main color should be orange

```html
<!DOCTYPE html>
<html lang="en">
<head>
<meta charset="utf-8">
<title>BVN Business Card</title>
<link href="https://fonts.googleapis.com/css2?family=Michroma&display=swap" rel="stylesheet">
<style>
  :root {
    --backdrop: #2b2b2d;
    --card: #121213;
    --card-band: #1b1b1d;
    --ink: #ffffff;
    --brand-blue: #0255a3;
    --name-blue: #1665c1;
    --brand-orange: #f37122;
    --brand-gold: #fece3e;
    --rule: #5a5a5e;
  }
  * { box-sizing: border-box; margin: 0; padding: 0; }
  html, body {
    width: 1200px;
    height: 800px;
    overflow: hidden;
    background: var(--backdrop);
    font-family: "Michroma", sans-serif;
    color: var(--ink);
  }
  .canvas {
    position: relative;
    width: 1200px;
    height: 800px;
  }
  .card {
    position: absolute;
    left: 330px;
    width: 520px;
    height: 290px;
    border-radius: 16px;
    background: var(--card);
    box-shadow: 0 10px 24px rgba(0,0,0,.45);
    overflow: hidden;
    text-align: center;
  }
  .card--front { top: 82px; }
  .card--back { top: 414px; }

  .front-band {
    position: absolute;
    left: 0; right: 0;
    top: 126px;
    height: 112px;
    background: var(--card-band);
  }
  .brand-mark {
    position: relative;
    display: inline-flex;
    align-items: center;
    gap: 10px;
    color: var(--brand-orange);
    font-weight: 400;
    line-height: 1;
  }
  .brand-mark__square {
    display: inline-block;
    background: var(--brand-blue);
  }
  .card--front .brand-mark {
    margin-top: 86px;
    font-size: 46px;
    letter-spacing: 2px;
  }
  .card--front .brand-mark__square { width: 34px; height: 34px; }

  .holder-name {
    position: relative;
    font-size: 27px;
    letter-spacing: 0.5px;
    line-height: 1;
  }
  .card--front .holder-name { margin-top: 30px; color: var(--ink); }
  .services {
    position: relative;
    font-size: 8.3px;
    letter-spacing: 0.2px;
    line-height: 1.45;
  }
  .card--front .services { margin-top: 12px; }

  .card--back .holder-name {
    margin-top: 78px;
    color: var(--name-blue);
    font-size: 27px;
  }
  .card--back .services {
    margin: 8px auto 0;
    width: 440px;
    font-size: 10.5px;
  }
  .divider {
    width: 250px;
    height: 1px;
    margin: 7px auto;
    background: var(--rule);
  }
  .contact {
    font-size: 15px;
    line-height: 1.35;
    letter-spacing: 0.3px;
  }
  .address {
    font-size: 13px;
    letter-spacing: 0.3px;
  }
  .card--back .brand-mark {
    margin-top: 16px;
    font-size: 16px;
    gap: 5px;
  }
  .card--back .brand-mark__square { width: 12px; height: 12px; }
</style>
</head>
<body>
<main class="canvas">
  <section class="card card--front" aria-label="Business card front">
    <div class="front-band"></div>
    <div class="brand-mark"><span class="brand-mark__square"></span>BVN</div>
    <h1 class="holder-name">MARTIN K. OSEI</h1>
    <p class="services">IT STRATEGIST / CONSULTANT - INFRASTRUCTURE - SYSTEMS - CYBERSECURITY</p>
  </section>

  <section class="card card--back" aria-label="Business card back">
    <h2 class="holder-name">MARTIN K. OSEI</h2>
    <p class="services">IT STRATEGIST / CONSULTANT - INFRASTRUCTURE<br>- SYSTEMS - CYBERSECURITY</p>
    <div class="divider"></div>
    <p class="contact">555.302.8846<br>MOSEI@BVNOREL.EXAMPLE</p>
    <div class="divider"></div>
    <p class="address">3817 WRENFIELD COURT PASADENA, CA 91877</p>
    <div class="brand-mark"><span class="brand-mark__square"></span>BVN</div>
  </section>
</main>
</body>
</html>
```